BOND WITH DERRIN FOR SPECIALISED ADHESIVE AND SEALANTS.

All that I am looking for is WORDING that can demonstrate to potential customers what the products can achieve and describing the various materials that this special adhesive will stick and why they need to choose it also a logo or even new name to fit in if financially possible
The size of the banner is unimportant as I only need help in getting the message over then I will adjust accordingly or pay the designer to complete.
As I am very limited in my knowledge of web design in fact it is non existent your help is paramount for the result.
This is a new project for me as I am now a young retired person who is looking for something different to follow.
Please let me know if the information I supply is in sufficient,
Best regards to all and in your design careers.
Updates

As pointed out to me that my request is to broad for a result,but I am not looking for words that describe a space shot, I am looking for suggestions to help me to put together some form of ad that helps me get the business off the ground ,I am no expert in marketing and design, so any format of words would be helpful,thank you all and remember, " you are the experts".

Target Market(s)

General public in the UK,and commercial business.
It would be used where there is a requirement to seal/or stick difficult materials or items but not large items like roofs/buildings etc.

Industry/Entity Type

Adhesive

Font styles to use
Sans Serif

Colors

Designer to choose colors to be used in the design.

Requirements
Must have
• To make people feel they will need the product or service maybe not initially but soon.
Nice to have
• This can be anything related to sticking or sealing different household products,
Should not have
• old fashioned font

```html
<!DOCTYPE html>
<html lang="en">
<head>
<meta charset="utf-8">
<title>Bond With Derrin – Adhesives &amp; Sealants</title>
<link rel="stylesheet" href="https://fonts.googleapis.com/css2?family=PT+Sans:wght@400;700&display=swap">
<style>
  :root {
    --brand-red: #bb1e2d;
    --brand-yellow: #fdea19;
    --ink: #111111;
    --paper: #ffffff;
    --photo-cool-a: #c9d3df;
    --photo-cool-b: #8a97a8;
    --photo-warm-a: #d9c2a0;
    --photo-warm-b: #a8774a;
  }
  * { box-sizing: border-box; margin: 0; padding: 0; }
  html, body {
    width: 1200px; height: 154px; overflow: hidden;
    background: var(--paper);
  }
  .banner {
    position: relative; width: 1200px; height: 154px; overflow: hidden;
    font-family: "PT Sans", Arial, sans-serif;
    font-weight: 700;
  }
  .banner__shapes { position: absolute; inset: 0; }
  .photo-fill-cool { stop-color: var(--photo-cool-a); }
  .photo-fill-cool-end { stop-color: var(--photo-cool-b); }
  .photo-fill-warm { stop-color: var(--photo-warm-a); }
  .photo-fill-warm-end { stop-color: var(--photo-warm-b); }
  .band-red { fill: var(--brand-red); }
  .tag-yellow { fill: var(--brand-yellow); }
  .band-white { fill: var(--paper); }
  .dot { fill: var(--brand-yellow); }

  .name-tag {
    position: absolute; left: 344px; top: 47px; height: 46px;
    display: flex; align-items: center; gap: 8px;
    color: var(--ink); font-size: 31px; letter-spacing: 0.2px;
    line-height: 1;
  }
  .name-tag__small { font-size: 22px; }

  .tagline {
    position: absolute; left: 339px; top: 111px;
    color: var(--paper); font-size: 26px; line-height: 1;
  }

  .benefits {
    position: absolute; top: 18px; left: 0; width: 1200px;
    list-style: none; color: var(--paper); font-size: 27px; line-height: 1;
  }
  .benefits li { position: absolute; }
  .benefits li:nth-child(1) { left: 702px; }
  .benefits li:nth-child(2) { left: 852px; }
  .benefits li:nth-child(3) { left: 1044px; }

  .call {
    position: absolute; left: 850px; top: 114px;
    color: var(--brand-red); font-size: 26px; line-height: 1;
    display: flex; align-items: baseline; gap: 8px;
  }
  .call__number { font-size: 22px; }
</style>
</head>
<body>
<div class="banner">
  <svg class="banner__shapes" width="1200" height="154" viewBox="0 0 1200 154" xmlns="http://www.w3.org/2000/svg">
    <defs>
      <linearGradient id="coolTone" x1="0" y1="0" x2="1" y2="1">
        <stop offset="0" class="photo-fill-cool"/>
        <stop offset="1" class="photo-fill-cool-end"/>
      </linearGradient>
      <linearGradient id="warmTone" x1="0" y1="0" x2="1" y2="1">
        <stop offset="0" class="photo-fill-warm"/>
        <stop offset="1" class="photo-fill-warm-end"/>
      </linearGradient>
    </defs>
    <rect x="2" y="2" width="196" height="150" fill="url(#coolTone)" role="img" aria-label="Photo: person brushing adhesive onto a white board"/>
    <rect x="203" y="2" width="230" height="150" fill="url(#warmTone)" role="img" aria-label="Photo: glue bottle applying adhesive to a wooden plank"/>
    <polygon class="band-red" points="408,0 1200,0 1200,154 324,154"/>
    <polygon class="tag-yellow" points="340,47 668,47 668,93 330,93"/>
    <polygon class="band-white" points="840,103 1200,103 1200,154 812,154"/>
    <circle class="dot" cx="691" cy="36" r="8"/>
    <circle class="dot" cx="841" cy="36" r="8"/>
    <circle class="dot" cx="1033" cy="36" r="8"/>
  </svg>

  <ul class="benefits">
    <li>Durable</li>
    <li>Non Toxic</li>
    <li>Affordable</li>
  </ul>

  <div class="name-tag">
    <span>BOND</span><span class="name-tag__small">WITH</span><span>DERRIN</span>
  </div>

  <p class="tagline">Adhesives &amp; Sealants</p>

  <p class="call"><span>CALL NOW</span><span class="call__number">555-555-5555</span></p>
</div>
</body>
</html>
```